Desktop publishing rework of financial advisor's corporate marketing brochure

We are a financial and strategic business consultancy to corporate clients in healthcare/ pharmaceuticals. We previously had a very "wordy" slide presentation which we now thinned down to a few messages. We have created mockups of the layouts for the pages. We have also 95% finalized all wording for the pages. What we need is redesign proposals for all of the pages 1, 2, 4, 5, 6. These proposals should reflect the current layout/ arrangement of objects; they should be much more professional and generally "better looking" than what we currently have. They shall replace existing graphics with better-looking more appropriate ones.
Many thanks all

Requirements
Must have
• Use the PPT file shared below as basis

```html
<!DOCTYPE html>
<html lang="en">
<head>
<meta charset="utf-8">
<title>Ashgrove Partners – Corporate Brochure</title>
<link href="https://fonts.googleapis.com/css2?family=EB+Garamond:ital,wght@0,400;0,600;0,700;1,400;1,600;1,700&display=swap" rel="stylesheet">
<style>
:root{
  --canvas:#4a4a4a;
  --sky:#5bbbe8;
  --cyan:#1bb0e6;
  --mid:#1a7fb8;
  --deep:#115a86;
  --navy:#0d3e62;
  --pale:#d6eef9;
  --soft:#8dcdee;
  --ink:#1d2b3a;
  --label:#17679b;
  --mute:#e6e9ee;
  --panel:#f1f2f4;
  --white:#ffffff;
}
*{margin:0;padding:0;box-sizing:border-box}
html,body{width:1200px;height:2375px;overflow:hidden;background:var(--canvas)}
body{font-family:"EB Garamond",Georgia,serif;color:var(--ink)}
.canvas{position:relative;width:1200px;height:2375px;background:var(--canvas)}
.cover{position:absolute;left:212px;top:65px;width:776px;height:582px;overflow:hidden}
.cover-photo{position:absolute;inset:0;background:linear-gradient(135deg,#f2f2f2 0%,#dcdcdc 45%,#9a9a9a 75%,#6d6d6d 100%)}
.cover-band{position:absolute;left:0;top:245px;width:638px;height:207px;background:rgba(66,178,228,.9)}
.cover-kicker{position:absolute;left:58px;top:48px;font-size:30px;font-weight:600;color:var(--white)}
.cover-title{position:absolute;left:58px;top:82px;font-size:52px;font-weight:700;color:var(--white)}
.cover-brand{position:absolute;left:426px;top:62px;width:300px;text-align:center;font-size:42px;font-weight:400;letter-spacing:9px;line-height:44px;color:#1a1a1a;border-top:2px solid #1a1a1a;padding-top:4px}
.cover-brand small{display:block;font-size:20px;letter-spacing:7px;line-height:24px}
.cover-web{position:absolute;left:66px;top:528px;font-size:18px;color:var(--white)}
.slide{position:absolute;width:495px;height:371px;background:var(--white);overflow:hidden}
.slide.is-blue{background:var(--sky)}
.slide-rule{position:absolute;left:0;right:0;top:40px;height:2px;background:var(--cyan)}
.is-blue .slide-rule{background:var(--white);top:48px}
.slide-title{position:absolute;left:32px;top:29px;padding:0 4px;background:var(--white);font-size:13.5px;font-weight:700;color:var(--navy);white-space:nowrap}
.slide-title em{color:var(--mid)}
.is-blue .slide-title{background:var(--sky);color:var(--white);line-height:16px;top:24px}
.is-blue .slide-title em{color:var(--white)}
.slide-tag{position:absolute;right:28px;top:14px;font-size:8px;font-style:italic;color:var(--ink)}
.is-blue .slide-tag{color:var(--white);top:24px}
.slide svg{position:absolute;left:0;top:0}
.team-col{position:absolute;top:56px;width:88px;text-align:center}
.team-photo{width:40px;height:58px;margin:0 auto;background:linear-gradient(#c9ced4,#8a929c)}
.team-logos{display:flex;justify-content:center;gap:3px;margin-top:8px;height:10px}
.team-logos span{width:16px;height:7px;background:#cfd3d8}
.team-name{margin-top:8px;font-size:6.5px;font-weight:700;color:var(--mid)}
.team-role{font-size:5.5px;font-style:italic;color:var(--mid)}
.team-summary{margin-top:5px;font-size:5px;font-style:italic;line-height:6.5px;color:var(--ink);height:40px}
.team-points{margin-top:12px;background:var(--panel);height:112px;padding:6px 5px;text-align:left;list-style:none}
.team-points li{font-size:4.6px;line-height:5.6px;margin-bottom:5px;padding-left:6px;position:relative}
.team-points li::before{content:"";position:absolute;left:0;top:2px;width:2px;height:2px;border-radius:50%;background:var(--mid)}
.team-footer{position:absolute;left:22px;top:340px;font-size:9.5px;font-weight:600}
.team-footer b{color:var(--mid)}
.map{position:absolute;left:90px;top:160px;width:320px;height:175px;background:radial-gradient(ellipse at center,#d9dbde 0%,#e9eaec 70%,#f6f6f6 100%);border-radius:40px}
.coverage-share{position:absolute;top:88px;font-size:26px;color:var(--deep);font-weight:400}
.revenue-note{position:absolute;left:38px;top:334px;font-size:12px;font-style:italic;font-weight:700}
</style>
</head>
<body>
<div class="canvas">

  <section class="cover">
    <div class="cover-photo" role="img" aria-label="Black and white photo looking up a glass skyscraper"></div>
    <div class="cover-brand">ASHGROVE<small>PARTNERS</small></div>
    <div class="cover-band">
      <div class="cover-kicker">Ashgrove Partners</div>
      <div class="cover-title">Beyond Advisory.</div>
    </div>
    <div class="cover-web">www.ashgrovepartners.com</div>
  </section>

  <section class="slide" style="left:86px;top:687px">
    <div class="slide-rule"></div>
    <div class="slide-title"><em>Healthcare-Focused Advisor</em> Founded by Former Granitefield Team</div>
    <div class="slide-tag">Ashgrove Partners</div>
    <svg width="495" height="371" viewBox="0 0 495 371" font-family="EB Garamond, serif">
      <rect x="31" y="66" width="142" height="138" fill="var(--cyan)"/>
      <rect x="173" y="66" width="142" height="138" fill="var(--mid)"/>
      <rect x="315" y="66" width="143" height="138" fill="var(--deep)"/>
      <rect x="31" y="204" width="142" height="139" fill="var(--navy)"/>
      <rect x="173" y="204" width="142" height="139" fill="var(--cyan)"/>
      <rect x="315" y="204" width="143" height="139" fill="var(--soft)"/>
      <polygon points="173,118 185,128 173,138" fill="var(--cyan)"/>
      <polygon points="315,118 327,128 315,138" fill="var(--mid)"/>
      <polygon points="380,204 392,204 386,216" fill="var(--deep)"/>
      <polygon points="315,255 303,265 315,275" fill="var(--soft)"/>
      <polygon points="173,255 185,265 173,275" fill="var(--navy)"/>
      <g fill="none" stroke="#fff" stroke-width="1.6">
        <circle cx="226" cy="98" r="7"/><circle cx="240" cy="88" r="6"/>
        <path d="M212 116 q10 -8 22 -2 l10 -6"/>
        <circle cx="352" cy="105" r="16"/><path d="M352 97 v16 M344 105 h16"/>
        <circle cx="78" cy="243" r="7"/><path d="M66 268 q12 -16 24 0 M92 236 l8 -6 l5 4 l8 -8"/>
        <circle cx="224" cy="236" r="8"/><circle cx="236" cy="250" r="8"/>
        <circle cx="356" cy="236" r="5"/><path d="M356 241 v14 M348 260 a10 4 0 1 0 16 0"/>
      </g>
      <g fill="#fff" text-anchor="end">
        <text x="160" y="160" font-size="24" font-weight="700">15</text>
        <text x="160" y="177" font-size="12" font-style="italic">Senior</text>
        <text x="160" y="192" font-size="12" font-style="italic">Professionals</text>
        <text x="302" y="160" font-size="24" font-weight="700">&gt;$150bn</text>
        <text x="302" y="177" font-size="12" font-style="italic">Transacted</text>
        <text x="302" y="192" font-size="12" font-style="italic">Deal Value</text>
        <text x="444" y="160" font-size="24" font-weight="700">15</text>
        <text x="444" y="177" font-size="12" font-style="italic">CEO Posts</text>
        <text x="444" y="192" font-size="12" font-style="italic">Held</text>
        <text x="160" y="297" font-size="24" font-weight="700">25 yrs</text>
        <text x="160" y="314" font-size="12" font-style="italic">Average</text>
        <text x="160" y="329" font-size="12" font-style="italic">Experience</text>
        <text x="302" y="297" font-size="24" font-weight="700">&gt;100</text>
        <text x="302" y="314" font-size="12" font-style="italic">Individual</text>
        <text x="302" y="329" font-size="12" font-style="italic">Transactions</text>
        <text x="444" y="297" font-size="24" font-weight="700">&gt;20</text>
        <text x="444" y="314" font-size="12" font-style="italic">C-Suite Positions</text>
        <text x="444" y="329" font-size="12" font-style="italic">Held</text>
      </g>
    </svg>
  </section>

  <section class="slide is-blue" style="left:618px;top:687px">
    <div class="slide-rule"></div>
    <div class="slide-title"><em>Outsourced Solution Delivery Office for Our Clients –</em><br>Enhanced Insight</div>
    <div class="slide-tag">Ashgrove Partners</div>
    <svg width="495" height="371" viewBox="0 0 495 371" font-family="EB Garamond, serif">
      <g fill="var(--pale)"><circle cx="111" cy="155" r="62"/><circle cx="250" cy="155" r="62"/><circle cx="393" cy="155" r="62"/></g>
      <g fill="none" stroke="var(--ink)" stroke-width="2">
        <circle cx="106" cy="150" r="16"/><path d="M117 162 l14 14 M96 154 l6 -6 l6 4 l8 -8"/>
        <path d="M228 160 l48 -22 l-14 48 l-10 -16 z M252 170 l24 -32"/>
        <circle cx="412" cy="137" r="9"/><path d="M408 133 l8 8 M416 133 l-8 8"/>
        <circle cx="378" cy="151" r="9"/><path d="M374 151 l3 3 l6 -6"/>
      </g>
      <g fill="var(--label)"><rect x="42" y="217" width="132" height="50"/><rect x="185" y="217" width="130" height="50"/><rect x="325" y="217" width="134" height="50"/></g>
      <g fill="#fff" font-size="11.5" font-weight="600" text-anchor="middle">
        <text x="108" y="238">Understand</text><text x="108" y="255">Situations</text>
        <text x="250" y="239">Identify</text><text x="250" y="256">Directions</text>
        <text x="392" y="236">Inform Decision</text><text x="392" y="253">Making</text>
      </g>
      <text x="250" y="322" text-anchor="middle" font-size="14.5" font-weight="700" fill="#fff">Baseline : Flawless Successful Execution Throughout</text>
    </svg>
  </section>

  <section class="slide" style="left:86px;top:1093px">
    <div class="slide-rule"></div>
    <div class="slide-title"><em>Deep Complementary</em> Senior Expertise</div>
    <div class="slide-tag">Ashgrove Partners</div>
    <svg width="495" height="371" viewBox="0 0 495 371" role="img" aria-label="Wall of former employer and client marks">
      <g fill="var(--mute)">
        <rect x="18" y="62" width="70" height="9"/><rect x="125" y="52" width="24" height="20"/><rect x="180" y="60" width="56" height="10"/><rect x="262" y="60" width="50" height="9"/><rect x="340" y="60" width="48" height="10"/><rect x="425" y="60" width="46" height="10"/>
        <rect x="22" y="98" width="66" height="9"/><rect x="112" y="95" width="44" height="12"/><rect x="172" y="95" width="60" height="12"/><rect x="248" y="92" width="62" height="16"/><rect x="338" y="95" width="44" height="11"/><rect x="398" y="90" width="24" height="20" rx="10"/><rect x="440" y="96" width="32" height="10"/>
        <rect x="32" y="122" width="16" height="16" rx="8"/><rect x="112" y="124" width="26" height="12"/><rect x="188" y="122" width="26" height="18"/><rect x="230" y="122" width="64" height="10"/><rect x="312" y="118" width="46" height="16"/><rect x="372" y="124" width="40" height="10"/><rect x="428" y="122" width="46" height="12"/>
        <rect x="18" y="156" width="60" height="10"/><rect x="100" y="156" width="40" height="10"/><rect x="358" y="152" width="56" height="14"/><rect x="420" y="154" width="54" height="10"/>
        <rect x="18" y="188" width="56" height="11"/><rect x="100" y="188" width="64" height="10"/><rect x="380" y="184" width="42" height="14"/><rect x="435" y="184" width="36" height="16"/>
        <rect x="28" y="214" width="22" height="22"/><rect x="70" y="220" width="40" height="10"/><rect x="124" y="218" width="60" height="12"/><rect x="350" y="220" width="66" height="9"/><rect x="436" y="222" width="42" height="14"/>
        <rect x="20" y="252" width="50" height="11"/><rect x="96" y="252" width="46" height="10"/><rect x="178" y="252" width="60" height="10"/><rect x="272" y="248" width="76" height="14"/><rect x="364" y="250" width="60" height="12"/><rect x="434" y="254" width="40" height="14"/>
        <rect x="22" y="282" width="44" height="10"/><rect x="104" y="282" width="44" height="10"/><rect x="228" y="276" width="60" height="18"/><rect x="372" y="284" width="54" height="12"/><rect x="440" y="282" width="34" height="12"/>
        <rect x="48" y="306" width="18" height="20"/><rect x="90" y="310" width="58" height="10"/><rect x="206" y="310" width="34" height="12"/><rect x="310" y="306" width="40" height="16"/><rect x="420" y="310" width="54" height="12"/>
        <rect x="24" y="338" width="46" height="12"/><rect x="110" y="336" width="44" height="16"/><rect x="180" y="338" width="54" height="12"/><rect x="256" y="334" width="34" height="16"/><rect x="318" y="338" width="42" height="12"/><rect x="378" y="338" width="40" height="10"/>
      </g>
      <g fill="none" stroke="var(--cyan)" stroke-width="3.5" stroke-linecap="round">
        <path d="M138 128 q-24 26 34 34"/><path d="M352 140 q-10 10 -20 16"/><path d="M184 310 q42 -4 52 -44"/>
      </g>
      <g fill="var(--cyan)">
        <polygon points="170,154 184,162 170,170"/><polygon points="332,148 342,160 326,162"/><polygon points="228,270 240,258 244,276"/>
      </g>
      <text x="250" y="202" text-anchor="middle" font-family="EB Garamond, serif" font-size="24" letter-spacing="5" fill="#1a1a1a">ASHGROVE</text>
      <text x="250" y="220" text-anchor="middle" font-family="EB Garamond, serif" font-size="11" letter-spacing="5" fill="#1a1a1a">PARTNERS</text>
    </svg>
  </section>

  <section class="slide" style="left:618px;top:1093px">
    <div class="slide-rule"></div>
    <div class="slide-title"><em>Outsourced Solution Delivery Office –</em> Areas of Work</div>
    <div class="slide-tag">Ashgrove Partners</div>
    <svg width="495" height="371" viewBox="0 0 495 371" font-family="EB Garamond, serif">
      <defs>
        <linearGradient id="blueFill" x1="0" y1="0" x2="0" y2="1"><stop offset="0" stop-color="#2a8cc4"/><stop offset="1" stop-color="#0d3e62"/></linearGradient>
      </defs>
      <rect x="40" y="62" width="145" height="196" rx="6" fill="url(#blueFill)" role="img" aria-label="Inward transaction funnel illustration"/>
      <rect x="310" y="62" width="145" height="196" rx="6" fill="url(#blueFill)" role="img" aria-label="Outward transaction funnel illustration"/>
      <rect x="190" y="80" width="120" height="140" rx="6" fill="url(#blueFill)" role="img" aria-label="Strategy cycle ring illustration"/>
      <g fill="#fff" font-size="9.5" font-weight="700" text-anchor="middle">
        <text x="112" y="88">Identify</text><text x="112" y="135">Screen</text><text x="112" y="173">Review</text><text x="112" y="211">Transact</text>
        <text x="382" y="88">Execute</text><text x="382" y="135">Approach</text><text x="382" y="173">Prepare</text><text x="382" y="211">Plan</text>
        <text x="250" y="112">Strategize</text><text x="250" y="134">Adjust</text><text x="250" y="156">Monitor</text><text x="250" y="178">Implement</text>
      </g>
      <ellipse cx="250" cy="236" rx="92" ry="20" fill="#a9dcf3"/>
      <ellipse cx="110" cy="285" rx="92" ry="18" fill="var(--sky)"/>
      <ellipse cx="390" cy="285" rx="92" ry="18" fill="var(--sky)"/>
      <g text-anchor="middle" fill="var(--ink)">
        <text x="250" y="229" font-size="8" font-style="italic">Senior Management:</text>
        <text x="250" y="241" font-size="8.5" font-weight="600">Companies · Businesses ·</text>
        <text x="250" y="252" font-size="8.5" font-weight="600">Portfolios · Products</text>
        <text x="110" y="281" font-size="8" font-style="italic">Inward Transactions:</text>
        <text x="110" y="293" font-size="8.5" font-weight="700">Buy · In-License · Partner · Invest</text>
        <text x="390" y="281" font-size="8" font-style="italic">Outward Transactions:</text>
        <text x="390" y="293" font-size="8.5" font-weight="700">Sell · Out-License · Partner · Re-Finance</text>
      </g>
      <text x="250" y="334" text-anchor="middle" font-size="14.5" font-weight="700" fill="var(--mid)">Baseline : Flawless Successful Execution Throughout</text>
    </svg>
  </section>

  <section class="slide" style="left:86px;top:1499px">
    <div class="slide-rule"></div>
    <div class="slide-title"><em>Unique Approach to Delivering</em> Client Success</div>
    <div class="slide-tag">Ashgrove Partners</div>
    <svg width="495" height="371" viewBox="0 0 495 371" font-family="EB Garamond, serif">
      <path d="M70 92 Q232 190 70 290" fill="none" stroke="#2aa3dc" stroke-width="11"/>
      <g fill="var(--deep)"><circle cx="70" cy="92" r="20"/><circle cx="141" cy="188" r="20"/><circle cx="70" cy="290" r="20"/></g>
      <g fill="none" stroke="#fff" stroke-width="1.6">
        <path d="M62 102 l8 -18 l8 18 z"/>
        <path d="M131 184 a10 10 0 0 1 18 -4 M151 192 a10 10 0 0 1 -18 4"/>
        <circle cx="64" cy="286" r="4"/><circle cx="76" cy="286" r="4"/>
      </g>
      <g font-size="13" fill="var(--ink)">
        <text x="46" y="128">Strategy</text>
        <text x="52" y="193">Transaction</text>
        <text x="20" y="268">Management</text>
      </g>
      <line x1="162" y1="188" x2="370" y2="188" stroke="var(--mid)" stroke-width="1.2"/>
      <g fill="var(--mid)" font-size="12.5" text-anchor="middle">
        <text x="213" y="184">CONSOLIDATE</text><text x="213" y="198">OUTPUT</text>
        <text x="323" y="172">Enable</text><text x="323" y="209">Pursue</text>
      </g>
      <circle cx="323" cy="188" r="6" fill="#fff" stroke="var(--mid)"/>
      <text x="323" y="192" text-anchor="middle" font-size="10" fill="var(--mid)">&amp;</text>
      <rect x="372" y="138" width="112" height="104" rx="6" fill="url(#targetFill)" role="img" aria-label="Target with arrow illustration"/>
      <defs><linearGradient id="targetFill" x1="0" y1="0" x2="1" y2="1"><stop offset="0" stop-color="#1bb0e6"/><stop offset="1" stop-color="#115a86"/></linearGradient></defs>
      <g fill="var(--mid)" font-size="12.5" text-anchor="middle">
        <text x="421" y="268">Successful</text><text x="421" y="283">Transactions &amp;</text><text x="421" y="298">Corporate</text><text x="421" y="313">Evolutions</text>
      </g>
    </svg>
  </section>

  <section class="slide" style="left:618px;top:1499px">
    <div class="slide-rule"></div>
    <div class="slide-title"><em>Key Team</em> Members</div>
    <div class="slide-tag">Ashgrove Partners</div>

    <div class="team-col" style="left:22px">
      <div class="team-photo" role="img" aria-label="Portrait of Omar Castellan"></div>
      <div class="team-logos"><span></span><span></span><span></span></div>
      <div class="team-name">Omar Castellan, MBBS</div>
      <div class="team-role">Founder &amp; Strategy Lead</div>
      <div class="team-summary">Senior biotech strategy advisor and negotiator with multidisciplinary strategic mindset</div>
      <ul class="team-points"><li>Led global healthcare advisory team</li><li>Prior roles at two global investment banks</li><li>Successful track record across market cycles</li><li>Hands-on clinical experience</li><li>Trained surgeon, BSc, MBBS, MBA</li></ul>
    </div>
    <div class="team-col" style="left:116px">
      <div class="team-photo" role="img" aria-label="Portrait of Felix Brandt"></div>
      <div class="team-logos"><span></span><span></span></div>
      <div class="team-name">Felix Brandt, MHMM</div>
      <div class="team-role">Founder &amp; Execution Lead</div>
      <div class="team-summary">Senior biotech transaction advisor with track record of successful execution in usual and turn-around situations</div>
      <ul class="team-points"><li>Buy-side and sell-side origination and execution</li><li>Deep coverage across healthcare segments</li><li>Financial and operational restructuring</li><li>Trained in business and medical science</li></ul>
    </div>
    <div class="team-col" style="left:210px">
      <div class="team-photo" role="img" aria-label="Portrait of Julian Harrow"></div>
      <div class="team-logos"><span></span><span></span><span></span></div>
      <div class="team-name">Julian Harrow</div>
      <div class="team-role">Head of Biopharma</div>
      <div class="team-summary">Successful serial CEO and board member with track record of successful financing, repositioning and exiting</div>
      <ul class="team-points"><li>Includes a major sale to a global pharma</li><li>Former corporate and business development leader at several pharma groups</li><li>Pharmacologist by training</li></ul>
    </div>
    <div class="team-col" style="left:304px">
      <div class="team-photo" role="img" aria-label="Portrait of Martin Vale"></div>
      <div class="team-logos"><span></span><span></span></div>
      <div class="team-name">Martin Vale, PhD</div>
      <div class="team-role">Portfolio and Strategy</div>
      <div class="team-summary">Successful corporate development strategist with track record in internal and external business building</div>
      <ul class="team-points"><li>Led development of various success strategies across the value chain</li><li>Former head of corporate development</li><li>Strategy consultant</li><li>Biochemist by training</li></ul>
    </div>
    <div class="team-col" style="left:398px">
      <div class="team-photo" role="img" aria-label="Portrait of Daniel Kestrel"></div>
      <div class="team-logos"><span></span><span></span><span></span></div>
      <div class="team-name">Daniel Kestrel, PhD</div>
      <div class="team-role">Industry Relations</div>
      <div class="team-summary">Senior corporate development leader with string of success in transaction origination and execution</div>
      <ul class="team-points"><li>Led creation of screening and evaluation committee</li><li>Corporate and business development leader</li><li>Biotech C-suite member</li><li>Product development positions</li><li>Pharmacologist by training</li></ul>
    </div>
    <div class="team-footer">Diverse Senior Team with <b>Deep Combined Domain and Transaction Expertise</b>.</div>
  </section>

  <section class="slide" style="left:352px;top:1908px">
    <div class="slide-rule"></div>
    <div class="slide-title"><em>Global</em> Coverage</div>
    <div class="slide-tag">Ashgrove Partners</div>
    <div class="coverage-share" style="left:122px">85%</div>
    <div class="coverage-share" style="left:249px">10%</div>
    <div class="coverage-share" style="left:378px">5%</div>
    <div class="map" role="img" aria-label="World map showing office locations in North America and Europe"></div>
    <svg width="495" height="371" viewBox="0 0 495 371">
      <rect x="146" y="212" width="36" height="16" rx="2" fill="#9aa3ad"/>
      <rect x="252" y="148" width="30" height="18" rx="2" fill="#8a6a7a"/>
    </svg>
    <div class="revenue-note">Revenue Split:</div>
  </section>

</div>
</body>
</html>
```